Professional & Modern Technology Business Card

We need a business card for our software/technology firm. Our services include Program/Project Management, Project Controls and Enterprise Analytics. Our clients are usually in the Aviation, Public Works, Transportation and Electric & Water Utility industries. We serve both public and private clients. Would like a very professional, conservative but somewhat modern design. Design, Develop, Deploy is the corporate tagline. We have two offices. The headquarters is in Atlanta, GA and a satellite office In Savannah, GA. Corporate Logo Attached.
Looking to do website and corporate brochure after the successful completion of this project. Would like to begin a working relationship with best designers.
Tagline: Design, Develop, Deploy
Website: www.quambelsystems.example
My Name: Delia Marchetti
My Title: CEO
Email: dmarchetti@quambelsystems.example
Atlanta Address:
87 Corliss Avenue, #2260
Atlanta, GA 30301
Office: 404.555.0178
Fax: 404.555.0143
Mobile: 404.555.0116
Savannah Address:
315 West Harrow Lane Street
Suite 720
Savannah, GA 31401
Office: 912.555.0162
Fax: 404.555.0143
Mobile: 404.555.0116
Please include the email address in your designs: dmarchetti@quambelsystems.example.
I appreciate everyone's design efforts. Just a few notes:
1. Please remove the mobile number from the cards
2. The backs of the cards can be utilized for writing notes. Make sure your design on the back of the card is conducive to clearly adding writing if needed.
3. No black backgrounds please
4. Only use the corporate logo on the front of the card. You can use portions of the logo design, but not the logo in totality.
Thank You
Conservative

```html
<!DOCTYPE html>
<html lang="en">
<head>
<meta charset="utf-8">
<title>Quambel Systems, Inc. — Business Card</title>
<link rel="stylesheet" href="https://fonts.googleapis.com/css2?family=Noto+Sans:wght@400;700&display=swap">
<style>
  :root {
    --page-bg: #ececec;
    --card-bg: #ffffff;
    --ink-dark: #333333;
    --ink-grey: #8a8a8a;
    --ink-label: #7a7a7a;
    --accent-yellow: #e6c52a;
    --rule: #3a3a3a;
  }
  * { margin: 0; padding: 0; box-sizing: border-box; }
  html, body {
    width: 1200px; height: 1001px; overflow: hidden;
    background: var(--page-bg);
    font-family: "Noto Sans", sans-serif;
  }
  .card {
    position: absolute; left: 34px; top: 169px;
    width: 1132px; height: 662px;
    background: var(--card-bg);
  }
  .brand {
    position: absolute; left: 72px; top: 128px;
    display: flex; align-items: center; gap: 18px;
  }
  .brand-mark { width: 56px; height: 56px; flex: none; }
  .brand-name {
    font-weight: 700; font-size: 46px; line-height: 1.05;
    color: var(--ink-dark); letter-spacing: -0.5px;
  }
  .person { position: absolute; left: 71px; top: 412px; }
  .person-name {
    font-weight: 700; font-size: 36px; color: var(--ink-dark);
    letter-spacing: 0.5px; line-height: 1.15;
  }
  .person-title { font-size: 30px; color: var(--ink-grey); line-height: 1.2; }
  .contact-list {
    position: absolute; left: 71px; top: 526px;
    list-style: none; font-size: 25px; color: var(--ink-grey);
  }
  .contact-list li { display: flex; align-items: center; gap: 16px; height: 37px; }
  .contact-list svg { width: 26px; height: 20px; fill: var(--ink-dark); flex: none; }
  .office {
    position: absolute; right: 70px; text-align: right;
    font-size: 25px; line-height: 37px; color: var(--ink-grey);
  }
  .office-atlanta { top: 96px; }
  .office-savannah { top: 381px; }
  .office-city {
    font-weight: 700; font-size: 27px; color: var(--ink-dark); letter-spacing: 0.5px;
  }
  .office strong { font-weight: 700; color: var(--ink-label); }
  .office-divider {
    position: absolute; left: 749px; top: 327px;
    width: 312px; height: 3px; background: var(--rule);
  }
</style>
</head>
<body>
  <main class="card">
    <div class="brand">
      <svg class="brand-mark" viewBox="0 0 56 56" aria-hidden="true">
        <circle cx="28" cy="28" r="26" fill="var(--accent-yellow)"/>
      </svg>
      <div class="brand-name">Quambel<br>Systems, Inc.</div>
    </div>

    <section class="person">
      <h1 class="person-name">DELIA MARCHETTI</h1>
      <p class="person-title">CEO</p>
    </section>

    <ul class="contact-list">
      <li>
        <svg viewBox="0 0 26 20" aria-hidden="true"><path d="M1 3h24v14H1z M1 3l12 9 12-9" fill="none" stroke="var(--ink-dark)" stroke-width="0"/><path d="M1 3h24L13 12z M1 5l12 9 12-9v12H1z"/></svg>
        <span>dmarchetti@quambelsystems.example</span>
      </li>
      <li>
        <svg viewBox="0 0 26 20" aria-hidden="true"><rect x="3" y="2" width="20" height="13" rx="1"/><rect x="0" y="16" width="26" height="3" rx="1"/></svg>
        <span>www.quambelsystems.example</span>
      </li>
    </ul>

    <address class="office office-atlanta">
      <div class="office-city">ATLANTA</div>
      <div>87 Corliss Avenue, #2260</div>
      <div>Atlanta, <strong>GA 30301</strong></div>
      <div><strong>Office:</strong> 404.555.0178</div>
      <div><strong>Fax:</strong> 404.555.0143</div>
    </address>

    <div class="office-divider"></div>

    <address class="office office-savannah">
      <div class="office-city">SAVANNAH</div>
      <div>315 West Harrow Lane Street</div>
      <div>Suite 720</div>
      <div>Savannah, <strong>GA 31401</strong></div>
      <div><strong>Office:</strong> 912.555.0162</div>
      <div><strong>Fax:</strong> 404.555.0143</div>
    </address>
  </main>
</body>
</html>
```